Masculine, visually appealing sales presentation for CPA firm

I have a basic power point that I use for sales presentations and I would like it to be updated to be more appealing and modern.

This is a presentation I give to real estate agents to help them close sales, save taxes, and resolve tax disputes. I would like the powerpoint to be updated to be more visually appealing. I have included the current powerpoint along with some of my logo files.

You don't have to use any of the pictures/clip art that is in the current power point. I only care that the words of the powerpoint make it to the new version.

Target Market(s)

Realtors, Real Estate Agents

Industry/Entity Type

Accounting

Requirements
Must have
• Visually appealing. I don't want it to look like I just took a template and made a normal powerpoint out of it. It should look custom.
Should not have
• Anything unprofessional, anything inconsistent with my brand

```html
<!DOCTYPE html>
<html lang="en">
<head>
<meta charset="utf-8">
<title>Introductions – Dale Whitaker, CPA</title>
<link href="https://fonts.googleapis.com/css2?family=Oswald:wght@300;400;600&display=swap" rel="stylesheet">
<style>
  :root {
    --slide-bg: #2b2b2b;
    --hex-fill: #000000;
    --accent-gold: #c98f3a;
    --text-light: #ffffff;
    --footer-bg: #ffffff;
    --footer-text: #1c1c1c;
  }
  * { margin: 0; padding: 0; box-sizing: border-box; }
  html, body {
    width: 1200px;
    height: 900px;
    overflow: hidden;
    background: var(--slide-bg);
  }
  .slide {
    position: relative;
    width: 1200px;
    height: 900px;
    background: var(--slide-bg);
    font-family: "Oswald", "Arial Narrow", sans-serif;
  }
  .slide-art {
    position: absolute;
    inset: 0;
  }
  .slide-content {
    position: absolute;
    left: 0;
    top: 0;
    width: 1200px;
    height: 838px;
    text-align: center;
  }
  .section-label {
    position: absolute;
    top: 142px;
    width: 100%;
    font-weight: 300;
    font-size: 31px;
    letter-spacing: 0.5px;
    color: var(--accent-gold);
  }
  .presenter-name {
    position: absolute;
    top: 323px;
    width: 100%;
    font-weight: 600;
    font-size: 46px;
    letter-spacing: 0.5px;
    color: var(--text-light);
  }
  .presenter-credential {
    position: absolute;
    top: 442px;
    width: 100%;
    font-weight: 300;
    font-size: 31px;
    line-height: 42px;
    color: var(--text-light);
  }
  .footer {
    position: absolute;
    left: 0;
    bottom: 0;
    width: 1200px;
    height: 62px;
    background: var(--footer-bg);
    display: flex;
    align-items: center;
    padding-left: 42px;
  }
  .brand {
    display: flex;
    align-items: center;
    gap: 12px;
    width: 338px;
  }
  .brand-mark {
    width: 28px;
    height: 28px;
    background: var(--footer-text);
  }
  .brand-name {
    font-weight: 600;
    font-size: 27px;
    color: var(--footer-text);
    letter-spacing: 0.3px;
  }
  .footer-org {
    font-weight: 300;
    font-size: 19px;
    color: var(--footer-text);
  }
</style>
</head>
<body>
  <main class="slide">
    <svg class="slide-art" width="1200" height="900" viewBox="0 0 1200 900" aria-hidden="true">
      <rect class="gold-frame" x="260" y="85" width="676" height="672" fill="none" stroke="var(--accent-gold)" stroke-width="6"/>
      <polygon class="title-hexagon" points="170,425 353,37 847,37 1033,425 847,817 353,817" fill="var(--hex-fill)"/>
    </svg>

    <section class="slide-content">
      <p class="section-label">INTRODUCTIONS</p>
      <h1 class="presenter-name">DALE WHITAKER, CPA</h1>
      <p class="presenter-credential">MEMBER OF THE NATIONAL ALLIANCE<br>OF TAX ISSUE RESOLVERS©</p>
    </section>

    <footer class="footer">
      <div class="brand">
        <span class="brand-mark"></span>
        <span class="brand-name">THE IRONWOOD CPA</span>
      </div>
      <span class="footer-org">NATIONAL ALLIANCE OF TAX ISSUE RESOLVERS©</span>
    </footer>
  </main>
</body>
</html>
```